Civic Counsel and Advocacy Alliance Event

Situation:
- Civic Counsel and Advocacy Alliance will host a fundraising event at Cellar of Amber Oak to create fundraising momentum for the year
- Event tickets will be $200
- The event will be a social/networking event for professional in the Detroit area
- DJ Lowell Varnick, a well know Detroit area DJ will DJ the event
- Hon. Marla Penwright-Osei, M.Ed. will be the featured speaker/host of the event
- CCA CEO will also be a speaker
- Proceeds from the event will go toward expungement, which is a hot top in Michigan, as s new expungement reform law has been enacted in the state

Objectives:
- Raise fund through ticket sales to support expungement and general CCA programs/services
- Gain event sponsors

Messaging:
- Highlight details about the event and the wine tasting/networking experience
- Inspire people to attend the event in support of a worthy cause
- Event Details:
- Event Name: The Vintage & Supper Soirée
o Date: Thursday, September 30, 2021
o Time: 5:30 PM – 8:30 PM
o Space limited, get your ticket today to ensure access to this exclusive event
o Sample various high-quality wines and custom pairings, while helping Civic Counsel and Advocacy Alliance make a difference in our community.
o Proceeds from the event will support Expungement, Domestic Violence prevention, an various CCA programs helping those in need of legal representation.

Target Market(s)

- Attorneys/Professionals in Southeast Michigan - Affluent donors/philanthropist

Industry/Entity Type

Legal/Networking Event

Colors
0054AA
0677BA
7BADD7
CADEEF
E8F1F8
FFF300
FFF600
FEFA6F
FFFEC7
FFFEE8

Requirements
Nice to have
• Must be fun and inviting

```html
<!DOCTYPE html>
<html lang="en">
<head>
<meta charset="utf-8">
<title>Wine Tasting – Civic Counsel and Advocacy Alliance</title>
<link href="https://fonts.googleapis.com/css2?family=Bebas+Neue&family=Cinzel:wght@500&family=Kaushan+Script&family=Oswald:wght@300;400;500&family=Source+Sans+3:wght@400;600&display=swap" rel="stylesheet">
<style>
  :root {
    --navy: #2b4593;
    --navy-deep: #1b2336;
    --navy-mid: #2c3650;
    --gold: #f2b632;
    --gold-deep: #d98a2b;
    --gold-line: #e9c77a;
    --ink-grey: #55565a;
    --paper: #ffffff;
    --paper-shade: #eef0f2;
    --backdrop: #e6e6e6;
    --ticket-yellow: #f6ea7a;
  }
  * { margin: 0; padding: 0; box-sizing: border-box; }
  html, body { width: 1200px; height: 817px; overflow: hidden; background: var(--backdrop); }
  .flyer {
    position: absolute; left: 300px; top: 18px;
    width: 612px; height: 795px;
    transform: scale(0.981); transform-origin: top left;
    background: radial-gradient(ellipse at 65% 35%, var(--paper) 40%, var(--paper-shade) 100%);
    overflow: hidden;
    font-family: "Source Sans 3", sans-serif;
    box-shadow: 0 4px 14px rgba(0,0,0,.18);
  }
  .gold-frame {
    position: absolute; left: 17px; top: 18px; width: 577px; height: 747px;
    border: 1.5px solid var(--gold-line); z-index: 5; pointer-events: none;
  }
  .hero-photo {
    position: absolute; left: 40px; top: 0; width: 225px; height: 468px;
    background: linear-gradient(160deg, #fbf7e6 0%, #efdf9c 40%, #d9b650 70%, #f4f1e8 100%);
    border-radius: 0 0 40% 40% / 0 0 12% 12%;
    opacity: .85;
  }
  .org-mark {
    position: absolute; left: 328px; top: 42px;
    display: flex; align-items: center; gap: 10px;
  }
  .org-mark .dot { width: 44px; height: 44px; border-radius: 50%; background: var(--navy); }
  .org-mark .name {
    font-family: "Source Sans 3", sans-serif; font-weight: 600;
    font-size: 13px; line-height: 1.15; color: var(--ink-grey); width: 170px;
  }
  .tagline {
    position: absolute; left: 305px; width: 280px; top: 95px; text-align: center;
    font-family: "Kaushan Script", cursive; font-size: 29px; color: var(--navy);
  }
  .title {
    position: absolute; left: 295px; width: 290px; text-align: center;
    font-family: "Cinzel", serif; font-weight: 500; line-height: 1;
    background: linear-gradient(180deg, var(--gold) 20%, var(--gold-deep) 100%);
    -webkit-background-clip: text; background-clip: text; color: transparent;
  }
  .title.wine { top: 137px; font-size: 66px; }
  .title.tasting { top: 195px; font-size: 66px; letter-spacing: -1px; }
  .date-row {
    position: absolute; left: 312px; top: 276px; display: flex; align-items: center; color: var(--navy);
  }
  .date-day { font-family: "Bebas Neue", sans-serif; font-size: 64px; line-height: 1; }
  .date-month { margin-left: 8px; font-family: "Oswald", sans-serif; line-height: 1.05; }
  .date-month b { display: block; font-weight: 500; font-size: 24px; }
  .date-month span { display: block; font-weight: 300; font-size: 21px; }
  .date-divider { width: 1px; height: 48px; background: var(--navy); margin: 0 8px 0 12px; opacity: .6; }
  .date-time { font-family: "Oswald", sans-serif; line-height: 1.45; }
  .date-time b { display: block; font-weight: 500; font-size: 17px; }
  .date-time span { display: block; font-weight: 300; font-size: 17px; text-transform: uppercase; }
  .ticket-badge {
    position: absolute; left: 202px; top: 333px; width: 116px; height: 116px; border-radius: 50%;
    background: radial-gradient(circle at 45% 45%, #fffbd0 0%, var(--ticket-yellow) 65%, rgba(246,234,122,.2) 100%);
    display: flex; flex-direction: column; align-items: center; justify-content: center;
    font-family: "Bebas Neue", sans-serif; color: var(--navy); font-size: 25px; line-height: .92;
  }
  .people { position: absolute; left: 318px; width: 258px; text-align: center; color: var(--ink-grey); }
  .people.speaker { top: 352px; }
  .people .person { font-family: "Oswald", sans-serif; font-weight: 300; font-size: 20px; letter-spacing: -.3px; text-transform: uppercase; }
  .people .role { font-size: 12.5px; margin-top: -2px; }
  .people-rule { position: absolute; left: 318px; top: 397px; width: 258px; height: 1px; background: #c9cacc; }
  .people.dj { top: 405px; }
  .intro-band {
    position: absolute; left: 0; top: 468px; width: 612px; height: 59px; background: var(--navy);
    color: #fff; font-size: 14.5px; line-height: 1.32; text-align: center;
    display: flex; align-items: center; justify-content: center; padding: 0 30px;
  }
  .photo-strip { position: absolute; left: 0; top: 527px; width: 612px; height: 178px; display: flex; }
  .photo-strip div { flex: 1; }
  .photo-bottles { background: linear-gradient(135deg, #6b4a34 0%, #2b2220 55%, #c9a98a 100%); }
  .photo-guests { background: linear-gradient(135deg, #8c6f73 0%, #4a4b55 50%, #b8a69a 100%); }
  .photo-platter { background: linear-gradient(135deg, #a4763c 0%, #d9c7a4 50%, #5c3a2e 100%); }
  .footer {
    position: absolute; left: 0; top: 690px; width: 612px; height: 105px;
    background: linear-gradient(180deg, var(--navy-mid) 0%, var(--navy-deep) 100%);
    border-top: 3px solid #f5f5f5;
  }
  .footer-copy {
    position: absolute; left: 40px; width: 532px; top: 22px; text-align: center;
    color: #fff; font-size: 13.2px; line-height: 1.2;
  }
  .cta-pill {
    position: absolute; left: 128px; top: 62px; width: 363px; height: 28px; border-radius: 14px;
    background: var(--navy); color: #fff; text-align: center;
    font-family: "Kaushan Script", cursive; font-size: 16px; line-height: 28px; z-index: 6;
  }
</style>
</head>
<body>
  <main class="flyer">
    <div class="hero-photo" role="img" aria-label="White wine being poured into a tall wine glass"></div>

    <div class="org-mark">
      <span class="dot"></span>
      <span class="name">Civic Counsel and Advocacy Alliance</span>
    </div>

    <p class="tagline">Come &amp; Wine With Us</p>
    <h1 class="title wine">WINE</h1>
    <h1 class="title tasting">TASTING</h1>

    <div class="date-row">
      <span class="date-day">30</span>
      <span class="date-month"><b>SEP</b><span>2021</span></span>
      <span class="date-divider"></span>
      <span class="date-time"><b>5:30 PM – 8:30 PM</b><span>Cellar of Amber Oak</span></span>
    </div>

    <div class="ticket-badge"><span>Event</span><span>Tickets</span><span>$200</span></div>

    <div class="people speaker">
      <p class="person">Hon. Marla Penwright-Osei, M.Ed.</p>
      <p class="role">speaker/host</p>
    </div>
    <div class="people-rule"></div>
    <div class="people dj"><p class="person">DJ Lowell Varnick</p></div>

    <div class="intro-band">
      <p>Sample various high-quality wines and custom pairings, while helping Civic Counsel and Advocacy Alliance make a difference in our community.</p>
    </div>

    <div class="photo-strip">
      <div class="photo-bottles" role="img" aria-label="Row of red wine bottles on a tasting table"></div>
      <div class="photo-guests" role="img" aria-label="Guests gathered at a wine tasting bar"></div>
      <div class="photo-platter" role="img" aria-label="Platter of bread, cheeses, nuts and grapes"></div>
    </div>

    <footer class="footer">
      <p class="footer-copy">Proceeds from the event will support Expungement, Domestic Violence prevention,<br>and various CCA programs helping those in need of legal representation.</p>
      <p class="cta-pill">Space limited. Get your ticket today!</p>
    </footer>

    <div class="gold-frame"></div>
  </main>
</body>
</html>
```